A design led business card for the construction industry

High-end business card to match logo. White logo on dark grey/off black to the front. Matching dark font on white to back, possibly with logo design again.

We offer construction and project management services to commercial and private clients in the UK. Projetcs range from newbuilds, conversion of listed buildings and refurbishments and extensions of existing homes. Our focus is on quality and attention to detail using the highest skills.

Contact Information for Business Card

Name; Dylan Marsh BSc
Position; Project Manager
Mobile; 07961 284 657
Tel; 01632 845192
email; dylan@craftvale.co.uk
web; www.craftvale.co.uk
Address; Harrowmere on Thames, KT4 7PX

Colors

Designer to choose only greyscale colors for use in the design.

Requirements
Must have
• To include the below description of the business,

CONSTRUCTION - PROJECT MANAGEMENT
Nice to have
• The posibility of the top back of the card being used as a ruler. So will have a measurement to scale in mm or an architect scale of 1:50
Should not have
• Should not be portrait

```html
<!DOCTYPE html>
<html lang="en">
<head>
<meta charset="utf-8">
<title>Craftvale Business Card</title>
<link rel="stylesheet" href="https://fonts.googleapis.com/css2?family=Arimo:wght@400;700&display=swap">
<style>
  :root {
    --stage: #0e0e0e;
    --paper: #f6f6f6;
    --ink: #111111;
    --ink-soft: #555555;
    --rule: #c9c9c9;
    --slate: #2a2a2b;
    --slate-band: #333334;
    --slate-line: #4a4a4b;
    --slate-text: #161616;
  }
  * { box-sizing: border-box; margin: 0; padding: 0; }
  html, body {
    width: 1200px;
    height: 820px;
    overflow: hidden;
    background: var(--stage);
    font-family: "Arimo", Arial, sans-serif;
  }
  .canvas {
    position: relative;
    width: 1200px;
    height: 820px;
  }
  .card {
    position: absolute;
    top: 262px;
    width: 520px;
    height: 297px;
  }
  /* Contact side */
  .card-contact {
    left: 50px;
    background: var(--paper);
    color: var(--ink);
  }
  .brand-block {
    position: absolute;
    left: 0;
    top: 0;
    width: 232px;
    height: 100%;
    display: flex;
    flex-direction: column;
    align-items: center;
    justify-content: center;
    gap: 18px;
  }
  .brand-square {
    width: 64px;
    height: 64px;
    border: 3px solid var(--ink);
  }
  .brand-name {
    font-size: 17px;
    font-weight: 400;
    letter-spacing: 7px;
    padding-left: 7px;
    color: var(--ink);
  }
  .divider {
    position: absolute;
    left: 242px;
    top: 78px;
    width: 1px;
    height: 140px;
    background: var(--rule);
  }
  .details {
    position: absolute;
    left: 268px;
    top: 62px;
    right: 16px;
  }
  .person-name {
    font-size: 17px;
    font-weight: 700;
    letter-spacing: 0.3px;
  }
  .person-name .credential {
    font-weight: 400;
  }
  .person-role {
    font-size: 13px;
    color: var(--ink-soft);
    margin-top: 2px;
  }
  .contact-list {
    list-style: none;
    margin-top: 14px;
  }
  .contact-list li {
    display: flex;
    align-items: center;
    gap: 7px;
    font-size: 13px;
    line-height: 18px;
    color: var(--ink-soft);
  }
  .contact-list svg {
    width: 12px;
    height: 12px;
    flex: none;
  }
  .address {
    font-size: 13px;
    color: var(--ink-soft);
    margin-top: 14px;
    white-space: nowrap;
  }
  /* Front side */
  .card-front {
    left: 630px;
    background: var(--slate);
    overflow: hidden;
  }
  .front-frame {
    position: absolute;
    left: 22px;
    top: 22px;
    width: 350px;
    height: 253px;
    border: 6px solid var(--slate-line);
    display: flex;
    align-items: center;
    justify-content: center;
    gap: 16px;
  }
  .front-square {
    width: 22px;
    height: 22px;
    background: var(--slate-line);
  }
  .front-name {
    font-size: 28px;
    font-weight: 400;
    letter-spacing: 8px;
    color: var(--slate-line);
  }
  .service-band {
    position: absolute;
    right: 0;
    top: 0;
    width: 126px;
    height: 100%;
    background: var(--slate-band);
    display: flex;
    align-items: center;
    justify-content: center;
  }
  .service-line {
    writing-mode: vertical-rl;
    transform: rotate(180deg);
    font-size: 15px;
    letter-spacing: 1.5px;
    line-height: 22px;
    color: var(--slate-text);
    text-shadow: 0 1px 0 #444;
    text-align: left;
  }
</style>
</head>
<body>
<main class="canvas">

  <section class="card card-contact">
    <div class="brand-block">
      <div class="brand-square"></div>
      <div class="brand-name">CRAFTVALE</div>
    </div>
    <div class="divider"></div>
    <div class="details">
      <p class="person-name">DYLAN MARSH <span class="credential">BSc</span></p>
      <p class="person-role">Project Manager</p>
      <ul class="contact-list">
        <li>
          <svg viewBox="0 0 12 12" aria-hidden="true"><rect x="3" y="0.8" width="6" height="10.4" rx="1" fill="none" stroke="#111" stroke-width="1.2"/><line x1="5" y1="9.4" x2="7" y2="9.4" stroke="#111" stroke-width="1"/></svg>
          07961 284 657
        </li>
        <li>
          <svg viewBox="0 0 12 12" aria-hidden="true"><path d="M3 1.2 L4.6 3.6 L3.6 4.8 C4.4 6.6 5.4 7.6 7.2 8.4 L8.4 7.4 L10.8 9 L9.8 10.8 C5.6 10.6 1.4 6.4 1.2 2.2 Z" fill="#111"/></svg>
          01632 845192
        </li>
        <li>
          <svg viewBox="0 0 12 12" aria-hidden="true"><rect x="0.8" y="2.4" width="10.4" height="7.4" fill="#111"/><path d="M1 2.8 L6 6.8 L11 2.8" fill="none" stroke="#f6f6f6" stroke-width="1"/></svg>
          dylan@craftvale.co.uk
        </li>
        <li>
          <svg viewBox="0 0 12 12" aria-hidden="true"><circle cx="6" cy="6" r="5" fill="none" stroke="#111" stroke-width="1.2"/><ellipse cx="6" cy="6" rx="2.2" ry="5" fill="none" stroke="#111" stroke-width="1"/><line x1="1" y1="6" x2="11" y2="6" stroke="#111" stroke-width="1"/></svg>
          www.craftvale.co.uk
        </li>
      </ul>
      <p class="address">Harrowmere on Thames, KT4 7PX</p>
    </div>
  </section>

  <section class="card card-front">
    <div class="front-frame">
      <div class="front-square"></div>
      <div class="front-name">CRAFTVALE</div>
    </div>
    <div class="service-band">
      <p class="service-line">CONSTRUCTION<br>PROJECT MANAGEMENT</p>
    </div>
  </section>

</main>
</body>
</html>
```